Business Card - Cooperate

Business Card for Quorin Management Consulting

Target Market(s)

Corparte - b2B

Industry/Entity Type

Management Consulting - Professional Services

Contact Information for Business Card

Company Name , Slogan , Dummy Address,

Requirements
Must have
• Reach your Full Potential

```html
<!DOCTYPE html>
<html lang="en">
<head>
<meta charset="utf-8">
<title>Quorin Management Consulting — Business Card</title>
<link href="https://fonts.googleapis.com/css2?family=Poppins:wght@400;600;700&display=swap" rel="stylesheet">
<style>
  :root {
    --bg: #2a2a2c;
    --navy: #1a1f8a;
    --royal: #1230a8;
    --azure: #0a66d8;
    --sky: #0a84ff;
    --green: #3cc81e;
    --ink: #111111;
    --paper: #ffffff;
  }
  * { margin: 0; padding: 0; box-sizing: border-box; }
  html, body { width: 1200px; height: 1015px; overflow: hidden; }
  body {
    background: var(--bg);
    font-family: "Poppins", sans-serif;
    display: flex;
    flex-direction: column;
    align-items: center;
    justify-content: center;
    gap: 50px;
  }
  .card {
    width: 680px;
    height: 388px;
    position: relative;
    overflow: hidden;
    box-shadow: 0 14px 30px rgba(0,0,0,.45);
  }
  /* Front */
  .card--front {
    background: linear-gradient(160deg, var(--navy) 0%, var(--royal) 45%, var(--azure) 100%);
    display: flex;
    align-items: center;
    justify-content: center;
  }
  .brand { display: flex; align-items: center; gap: 22px; }
  .brand__dot {
    width: 74px; height: 74px; border-radius: 50%;
    background: var(--paper);
  }
  .brand__text { display: flex; flex-direction: column; }
  .brand__name {
    color: var(--paper);
    font-weight: 600;
    font-size: 78px;
    line-height: 1;
    letter-spacing: 1px;
  }
  .brand__tagline {
    color: var(--paper);
    font-weight: 600;
    font-size: 12.5px;
    letter-spacing: 3.6px;
    margin-top: 8px;
    text-transform: uppercase;
  }
  /* Back */
  .card--back { background: var(--paper); }
  .accent-block {
    position: absolute;
    left: 0; top: 122px;
    width: 58px; height: 44px;
    background: linear-gradient(160deg, var(--navy), var(--azure));
  }
  .holder { position: absolute; left: 82px; top: 112px; }
  .holder__name {
    color: var(--royal);
    font-weight: 700;
    font-size: 30px;
    line-height: 1.1;
  }
  .holder__role {
    color: var(--green);
    font-size: 19px;
    line-height: 1.2;
  }
  .contacts {
    list-style: none;
    position: absolute; left: 82px; top: 200px;
    font-size: 17px; color: var(--ink); line-height: 1.45;
  }
  .contacts li { display: flex; align-items: center; gap: 10px; }
  .contacts svg { width: 16px; height: 16px; fill: var(--royal); flex: none; }
  .contacts .site-name { color: var(--royal); }
  .address {
    position: absolute; left: 82px; top: 298px;
    font-size: 17px; color: var(--ink); line-height: 1.3;
  }
  .mark {
    position: absolute; right: 58px; top: 70px;
    display: flex; flex-direction: column; align-items: center; gap: 14px;
  }
  .mark__circle {
    width: 170px; height: 170px; border-radius: 50%;
    background: linear-gradient(200deg, var(--navy), var(--sky) 60%, var(--green));
  }
  .mark__name {
    color: var(--navy); font-weight: 600; font-size: 34px; line-height: 1;
  }
</style>
</head>
<body>
  <section class="card card--front" aria-label="Business card front">
    <div class="brand">
      <span class="brand__dot"></span>
      <div class="brand__text">
        <span class="brand__name">quorin</span>
        <span class="brand__tagline">Reach your full potential</span>
      </div>
    </div>
  </section>

  <section class="card card--back" aria-label="Business card back">
    <span class="accent-block"></span>
    <div class="holder">
      <p class="holder__name">Daniel Marsh</p>
      <p class="holder__role">Managing Director</p>
    </div>
    <ul class="contacts">
      <li>
        <svg viewBox="0 0 24 24" aria-hidden="true"><path d="M6.6 10.8a15.1 15.1 0 0 0 6.6 6.6l2.2-2.2a1 1 0 0 1 1-.25 11.4 11.4 0 0 0 3.6.57 1 1 0 0 1 1 1V20a1 1 0 0 1-1 1A17 17 0 0 1 3 4a1 1 0 0 1 1-1h3.5a1 1 0 0 1 1 1c0 1.25.2 2.45.57 3.57a1 1 0 0 1-.25 1z"/></svg>
        041-570 382 916
      </li>
      <li>
        <svg viewBox="0 0 24 24" aria-hidden="true"><path d="M2 5h20v14H2zm2 2v.4l8 5 8-5V7z"/></svg>
        hello@quorinmc.com
      </li>
      <li>
        <svg viewBox="0 0 24 24" aria-hidden="true"><path d="M12 2a10 10 0 1 0 0 20 10 10 0 0 0 0-20zm6.9 6h-3a15 15 0 0 0-1.3-3.9A8 8 0 0 1 18.9 8zM12 4c.8 1.2 1.5 2.5 1.9 4h-3.8c.4-1.5 1.1-2.8 1.9-4zM4.3 14a8 8 0 0 1 0-4h3.4a16 16 0 0 0 0 4zm.8 2h3a15 15 0 0 0 1.3 3.9A8 8 0 0 1 5.1 16zm3-8h-3a8 8 0 0 1 4.3-3.9A15 15 0 0 0 8.1 8zM12 20c-.8-1.2-1.5-2.5-1.9-4h3.8c-.4 1.5-1.1 2.8-1.9 4zm2.3-6H9.7a14 14 0 0 1 0-4h4.6a14 14 0 0 1 0 4zm.3 5.9a15 15 0 0 0 1.3-3.9h3a8 8 0 0 1-4.3 3.9zm1.7-5.9a16 16 0 0 0 0-4h3.4a8 8 0 0 1 0 4z"/></svg>
        <span>www.<span class="site-name">quorinmc</span>.com</span>
      </li>
    </ul>
    <p class="address">421, Address line goes here<br>45452, Country Name</p>
    <div class="mark">
      <span class="mark__circle"></span>
      <span class="mark__name">quorin</span>
    </div>
  </section>
</body>
</html>
```